Long Established Local Fencing (not swords) Business needs fresh Business Cards

We need fresh double sided business cards for our Fencing Construction business, we are looking for something with our new logo design added, and maybe a photo background ?
We recently had cards made from Cardlyne and we were horrified with what we got back, the quality was terrible, so am looking for high quality format for good printing company to make.
We install Steelmora, Timber paling, Aluminium Slat Screening, Picket (timber and aluminium) and most other fencing installations.
Our website is brankelrails.com.au should you like to learn a bit more.
We do have logo in other formats if required.
We have been in business for over 35 years and we have used this as a "motto" it is on our signage

Industry/Entity Type

Construction

Contact Information for Business Card

Open to ideas, we need 3 x different cards, one generic with no name and 2 x others each with 1 of our bosses name on each, I will put into upload files.

Colors
ec1f27
000000
606060
f5f5f5

Requirements
Must have
• Company Name and Logo
• Address
• Contact details, phone, website, email etc
• Small space to write notes when leaving card at residence
Nice to have
• Our motto "Servicing the Peninsula for over 35 years"

```html
<!DOCTYPE html>
<html lang="en">
<head>
<meta charset="utf-8">
<title>Brankel Rails – Business Cards</title>
<link href="https://fonts.googleapis.com/css2?family=Open+Sans:wght@400;600&family=Montserrat:wght@800&family=Tinos&display=swap" rel="stylesheet">
<style>
  :root {
    --brand-red: #ec1f27;
    --brand-black: #000000;
    --brand-grey: #606060;
    --brand-light: #f5f5f5;
    --stage: #2a2c31;
    --card-dark: #1c1f1d;
  }
  * { box-sizing: border-box; margin: 0; padding: 0; }
  html, body { width: 1200px; height: 900px; overflow: hidden; }
  body {
    background: var(--stage);
    font-family: "Open Sans", sans-serif;
    position: relative;
  }
  .card {
    position: absolute;
    width: 520px;
    height: 300px;
    border-radius: 16px;
    overflow: hidden;
    box-shadow: 0 14px 30px rgba(0,0,0,.45);
  }
  /* Front */
  .card-front { left: 50px; top: 300px; }
  .front-photo {
    position: absolute; inset: 0;
    background: linear-gradient(160deg, #4d6a3a 0%, #3a4a3c 22%, #55606c 40%, #4a5563 65%, #5a4638 82%, #3f4e5a 100%);
  }
  .front-shade { position: absolute; inset: 0; background: rgba(0,0,0,.35); }
  .front-content { position: absolute; left: 40px; top: 48px; right: 30px; }
  .brand {
    display: flex; align-items: center; gap: 12px;
    margin-left: 120px; margin-bottom: 26px;
  }
  .brand-dot { width: 26px; height: 26px; border-radius: 50%; background: var(--brand-red); }
  .brand-name {
    font-family: "Montserrat", sans-serif; font-weight: 800;
    font-size: 30px; letter-spacing: 1px; text-transform: uppercase;
    color: var(--brand-black);
    background: none;
  }
  .person-name { font-size: 46px; color: var(--brand-red); line-height: 1.05; }
  .person-phone { font-size: 32px; color: var(--brand-light); margin-top: 10px; }
  .person-address {
    font-family: "Tinos", serif; font-size: 24px; color: #9aa1aa; margin-top: 10px;
  }
  /* Back */
  .card-back { left: 630px; top: 300px; background: var(--card-dark); }
  .back-photo {
    position: absolute; inset: 0;
    background: linear-gradient(120deg, #2c3a2e 0%, #1e2620 45%, #2a2d2b 100%);
  }
  .back-shape { position: absolute; inset: 0; }
  .note-lines { position: absolute; left: 30px; top: 48px; width: 190px; }
  .note-line { border-bottom: 2px dashed #2b2b2b; height: 46px; }
  .contact-list {
    position: absolute; left: 262px; top: 60px; list-style: none;
    color: var(--brand-light); font-size: 14px;
  }
  .contact-item { display: flex; align-items: center; gap: 12px; margin-bottom: 18px; line-height: 1.3; }
  .contact-icon {
    flex: none; width: 28px; height: 28px; border-radius: 50%;
    border: 2px solid #5a5a5a; display: flex; align-items: center; justify-content: center;
  }
</style>
</head>
<body>

<section class="card card-front">
  <div class="front-photo" role="img" aria-label="Photo of a corrugated steel fence with timber rails and trees behind"></div>
  <div class="front-shade"></div>
  <div class="front-content">
    <div class="brand">
      <span class="brand-dot"></span>
      <span class="brand-name">Brankel Rails</span>
    </div>
    <p class="person-name">Dale Merritt</p>
    <p class="person-phone">43 520 618</p>
    <p class="person-address">27 Kestrel Ave Brankel</p>
  </div>
</section>

<section class="card card-back">
  <div class="back-photo" role="img" aria-label="Photo of a dark slatted fence beside a driveway"></div>
  <svg class="back-shape" viewBox="0 0 520 300" preserveAspectRatio="none" aria-hidden="true">
    <path d="M0 0 H420 C330 0 300 40 270 110 C245 170 200 210 140 300 H0 Z" fill="var(--brand-grey)"/>
  </svg>
  <div class="note-lines">
    <div class="note-line"></div>
    <div class="note-line"></div>
    <div class="note-line"></div>
    <div class="note-line"></div>
  </div>
  <ul class="contact-list">
    <li class="contact-item">
      <span class="contact-icon">
        <svg width="14" height="14" viewBox="0 0 24 24"><path fill="#ec1f27" d="M6.6 10.8a15 15 0 0 0 6.6 6.6l2.2-2.2a1 1 0 0 1 1-.25 11.4 11.4 0 0 0 3.6.57 1 1 0 0 1 1 1V20a1 1 0 0 1-1 1A17 17 0 0 1 3 4a1 1 0 0 1 1-1h3.5a1 1 0 0 1 1 1c0 1.25.2 2.45.57 3.57a1 1 0 0 1-.25 1z"/></svg>
      </span>
      <span>(02)43520618<br>0427 308 462</span>
    </li>
    <li class="contact-item">
      <span class="contact-icon">
        <svg width="14" height="14" viewBox="0 0 24 24"><circle cx="10" cy="10" r="6" fill="none" stroke="#ec1f27" stroke-width="3"/><path d="M14.5 14.5 21 21" stroke="#ec1f27" stroke-width="3"/></svg>
      </span>
      <span>brankelrails.com.au</span>
    </li>
    <li class="contact-item">
      <span class="contact-icon">
        <svg width="14" height="14" viewBox="0 0 24 24"><rect x="2" y="5" width="20" height="14" fill="#ec1f27"/><path d="M2 5l10 8 10-8" fill="none" stroke="#fff" stroke-width="1.5"/></svg>
      </span>
      <span>brankelrails@mailhub.com.au</span>
    </li>
    <li class="contact-item">
      <span class="contact-icon">
        <svg width="14" height="14" viewBox="0 0 24 24"><path fill="#ec1f27" d="M12 2a7 7 0 0 0-7 7c0 5 7 13 7 13s7-8 7-13a7 7 0 0 0-7-7z"/><circle cx="12" cy="9" r="2.5" fill="#fff"/></svg>
      </span>
      <span>PO Box 418<br>Harrowvale NSW 2281</span>
    </li>
  </ul>
</section>

</body>
</html>
```